Facelink Ad for “5 Day Personal Image Sprint”

I would like a Facelink ad graphic for this offer:
https://www.morvitaplan.com/5-day-personal-branding-challenge
Please include my photo- I have attached images to use (remove the background)
The big selling points are the three focus points during the challenge (Facelink Page, ProNetwork profile and the web site) and the cost is only $5.40
I will choose the winner who submits one ad, and then the winner will be asked to provide two variations of the ad graphic so I can test all three graphics.
Thank you, I’m looking forward to seeing your ideas and designs!

```html
<!DOCTYPE html>
<html lang="en">
<head>
<meta charset="utf-8">
<title>5 Day Personal Image Sprint – Ad Variations</title>
<link href="https://fonts.googleapis.com/css2?family=Montserrat:wght@300;800&family=Allura&family=Oswald:wght@500&family=Roboto:wght@400;500&display=swap" rel="stylesheet">
<style>
  :root {
    --stage: #1b1b1b;
    --paper: #ffffff;
    --blue: #1b4ea6;
    --blue-deep: #133f8f;
    --blue-light: #3d8ccc;
    --photo-top: #c9a898;
    --photo-mid: #2d3237;
    --photo-low: #283a5c;
  }
  * { margin: 0; padding: 0; box-sizing: border-box; }
  html, body { width: 759px; height: 1200px; overflow: hidden; background: var(--stage); }
  .ad {
    position: absolute; left: 129px; width: 500px; height: 499px;
    background: var(--paper); overflow: hidden; color: var(--blue);
    font-family: "Roboto", sans-serif;
  }
  .ad--first { top: 83px; }
  .ad--second { top: 631px; }

  .headline { position: absolute; top: 26px; left: 29px; display: flex; align-items: flex-start; z-index: 3; }
  .headline__num { font-family: "Montserrat", sans-serif; font-weight: 800; font-size: 74px; line-height: 1; letter-spacing: -3px; }
  .headline__day { font-family: "Montserrat", sans-serif; font-weight: 300; font-size: 74px; line-height: 1; letter-spacing: -2px; }
  .headline__words { margin-left: 8px; margin-top: 5px; font-family: "Montserrat", sans-serif; font-weight: 800; font-size: 36px; line-height: 0.98; }
  .headline__script {
    position: absolute; left: 26px; top: 78px; z-index: 3;
    font-family: "Allura", cursive; font-size: 150px; line-height: 1; color: var(--blue);
  }

  .photo { position: absolute; z-index: 1; }
  .ad--first .photo { left: 202px; top: 99px; width: 298px; height: 400px; }
  .ad--second .photo { left: 88px; top: 166px; width: 323px; height: 333px; }
  .photo svg { width: 100%; height: 100%; display: block; }

  .price-pill {
    position: absolute; left: 0; top: 214px; width: 250px; height: 62px; z-index: 2;
    background: var(--blue); border-radius: 0 31px 31px 0;
    box-shadow: 0 6px 14px rgba(19,63,143,.25);
    font-family: "Oswald", sans-serif; font-size: 42px; color: #fff;
    display: flex; align-items: center; padding-left: 27px; letter-spacing: 0.5px;
  }
  .intro { position: absolute; left: 23px; top: 289px; width: 205px; z-index: 2;
    font-size: 12px; line-height: 1.2; color: var(--blue-light); }
  .checklist { position: absolute; left: 24px; top: 343px; list-style: none; z-index: 2; }
  .checklist li { display: flex; align-items: flex-start; gap: 10px; margin-bottom: 13px;
    font-size: 11px; line-height: 1.2; text-transform: uppercase; width: 190px; }
  .checklist li:nth-child(2) { margin-bottom: 9px; }
  .checklist svg { flex: none; width: 19px; height: 17px; }
  .brand { position: absolute; left: 24px; top: 457px; display: flex; align-items: center; gap: 6px;
    font-size: 13px; font-weight: 500; color: var(--blue); text-transform: uppercase; z-index: 2; }
  .brand__dot { width: 12px; height: 12px; border-radius: 50%; background: var(--blue-light); }

  .price-band {
    position: absolute; left: 0; top: 212px; width: 500px; height: 87px; z-index: 0;
    background: var(--blue); box-shadow: 0 -2px 10px rgba(255,255,255,.6);
  }
  .price-band__only { position: absolute; left: 18px; top: 14px; transform-origin: left top;
    transform: rotate(-90deg) translateX(-60px);
    font-family: "Oswald", sans-serif; font-size: 21px; color: #fff; letter-spacing: 1px; }
  .price-band__amount { position: absolute; left: 42px; top: 4px; font-family: "Oswald", sans-serif;
    font-size: 66px; line-height: 1.15; color: #fff; letter-spacing: -1px; }
  .price-band__pitch { position: absolute; left: 296px; top: 19px; width: 196px;
    font-size: 9.4px; line-height: 1.22; color: #fff; text-align: right; }

  .gets { position: absolute; left: 19px; top: 332px; z-index: 2; }
  .gets__title { font-size: 13px; color: var(--blue-light); text-transform: uppercase; margin-bottom: 11px; }
  .gets ul { list-style: none; }
  .gets li { font-size: 10.5px; font-weight: 500; line-height: 1.2; text-transform: uppercase; width: 88px; margin-bottom: 12px; }
  .brand-large { position: absolute; right: 14px; top: 340px; z-index: 2; text-align: right;
    font-family: "Montserrat", sans-serif; font-weight: 800; font-size: 22px; line-height: 1.1; color: var(--blue); text-transform: uppercase; }
</style>
</head>
<body>

<section class="ad ad--first">
  <div class="headline">
    <span class="headline__num">5</span><span class="headline__day">DAY</span>
    <span class="headline__words">PERSONAL<br>IMAGE</span>
  </div>
  <div class="headline__script">Sprint</div>

  <div class="photo" role="img" aria-label="Photo of the coach in a dark t-shirt and jeans, seated, background removed">
    <svg viewBox="0 0 298 400" preserveAspectRatio="none">
      <defs>
        <linearGradient id="p1" x1="0" y1="0" x2="0" y2="1">
          <stop offset="0" stop-color="var(--photo-top)"/>
          <stop offset="0.3" stop-color="var(--photo-mid)"/>
          <stop offset="0.8" stop-color="var(--photo-mid)"/>
          <stop offset="1" stop-color="var(--photo-low)"/>
        </linearGradient>
      </defs>
      <path d="M150 0 C185 0 200 30 198 70 L200 100 C250 110 290 130 298 150 L298 400 L0 400 L0 330 C15 240 40 150 95 115 L110 100 L105 70 C102 30 118 0 150 0 Z" fill="url(#p1)"/>
    </svg>
  </div>

  <div class="price-pill">ONLY $5.40</div>
  <p class="intro">When The Five Days Are Done, You’ll Have These Assets Complete and Ready to Grow:</p>
  <ul class="checklist">
    <li><svg viewBox="0 0 19 17"><circle cx="8.5" cy="9" r="7" fill="none" stroke="var(--blue)" stroke-width="1.4"/><path d="M4.5 9 L8 12.5 L17 2.5" fill="none" stroke="var(--blue)" stroke-width="1.8"/></svg>A professional Facelink business page</li>
    <li><svg viewBox="0 0 19 17"><circle cx="8.5" cy="9" r="7" fill="none" stroke="var(--blue)" stroke-width="1.4"/><path d="M4.5 9 L8 12.5 L17 2.5" fill="none" stroke="var(--blue)" stroke-width="1.8"/></svg>An attractive ProNetwork profile</li>
    <li><svg viewBox="0 0 19 17"><circle cx="8.5" cy="9" r="7" fill="none" stroke="var(--blue)" stroke-width="1.4"/><path d="M4.5 9 L8 12.5 L17 2.5" fill="none" stroke="var(--blue)" stroke-width="1.8"/></svg>Your very own website!</li>
  </ul>
  <div class="brand"><span class="brand__dot"></span>Morvita Group</div>
</section>

<section class="ad ad--second">
  <div class="headline">
    <span class="headline__num">5</span><span class="headline__day">DAY</span>
    <span class="headline__words">PERSONAL<br>IMAGE</span>
  </div>
  <div class="headline__script">Sprint</div>

  <div class="price-band">
    <span class="price-band__only">ONLY</span>
    <span class="price-band__amount">$5.40</span>
    <p class="price-band__pitch">When you join my brand new “5 Day Personal Image Action Plan” you’re working with me, in bite-size steps, to get your online presence built out and ready for growth!</p>
  </div>

  <div class="photo" role="img" aria-label="Photo of the coach in a dark t-shirt, seated facing forward, background removed">
    <svg viewBox="0 0 323 333" preserveAspectRatio="none">
      <defs>
        <linearGradient id="p2" x1="0" y1="0" x2="0" y2="1">
          <stop offset="0" stop-color="var(--photo-top)"/>
          <stop offset="0.3" stop-color="var(--photo-mid)"/>
          <stop offset="0.85" stop-color="var(--photo-mid)"/>
          <stop offset="1" stop-color="var(--photo-low)"/>
        </linearGradient>
      </defs>
      <path d="M152 0 C176 0 190 20 190 50 L188 85 C192 100 200 112 202 120 L202 133 C245 140 275 150 290 175 L310 333 L22 333 L30 300 L35 175 C45 150 80 140 104 133 L104 120 C108 110 116 100 116 85 L114 50 C114 20 128 0 152 0 Z" fill="url(#p2)"/>
    </svg>
  </div>

  <div class="gets">
    <p class="gets__title">You’ll get</p>
    <ul>
      <li>A professional Facelink business page</li>
      <li>An attractive ProNetwork profile</li>
      <li>Your very own website!</li>
    </ul>
  </div>
  <div class="brand-large">Morvita<br>Group</div>
</section>

</body>
</html>
```